Rabbit Meat Label

We need a label for a shrink-wrapped tray of rabbit. The label does not need to be fancy, we just want a simple sticker to show customers a mock-up of what it may look like. The label is approximately 5" x 2.75". The label will go on top of the rabbit, so it will not lay flat. Please take that into consideration

The rabbit specifically is farm raised. Whole cut-up with 2 fore-legs, 2 hind legs and back.

There is nutritional information on the back, so please mention that somewhere on the label.

Industry/Entity Type

Farm

Requirements
Must have
• Please leave spaces for QLMV seals and other misc items. They are about 0.5" squares.
Should not have
• Do not have anything like "Made in the USA" or "All Natural." This will be added later, if need be.

```html
<!DOCTYPE html>
<html lang="en">
<head>
<meta charset="utf-8">
<title>Farm Raised Rabbits – Tray Label</title>
<link rel="stylesheet" href="https://fonts.googleapis.com/css2?family=Noticia+Text:ital,wght@1,400&family=Oswald:wght@400&family=Open+Sans:wght@400&display=swap">
<style>
  :root {
    --bg-top: #ffffff;
    --bg-bottom: #e4e4e4;
    --gold: #c9a63a;
    --seal-gold: #c8a842;
    --pink: #d8398f;
    --pink-deep: #b02a78;
    --green: #1f4a22;
    --black: #0b0d0b;
    --white: #ffffff;
    --art-shade: #e6e6e6;
  }
  * { margin: 0; padding: 0; box-sizing: border-box; }
  html, body { width: 1200px; height: 848px; overflow: hidden; }
  body {
    background: linear-gradient(to bottom, var(--bg-top) 0%, var(--bg-bottom) 100%);
    position: relative;
  }
  .label {
    position: absolute;
    left: 328px; top: 264px;
    width: 513px; height: 282px;
    border: 3px solid var(--gold);
    overflow: hidden;
    background: var(--black);
  }
  .band { position: absolute; left: 0; width: 100%; }
  .band--pasture {
    top: 0; height: 121px;
    background: linear-gradient(to bottom, var(--pink) 0%, #d13f92 55%, var(--pink-deep) 100%);
  }
  .band--cut {
    top: 121px; height: 46px;
    background: var(--green);
  }
  .band--name {
    top: 167px; height: 115px;
    background: var(--black);
  }
  .title-farm {
    position: absolute; left: 18px; top: 27px;
    font-family: 'Noticia Text', Georgia, serif;
    font-style: italic;
    font-size: 62px; line-height: 1;
    color: var(--white);
    letter-spacing: 1.5px;
    white-space: nowrap;
  }
  .cut-description {
    position: absolute; left: 14px; top: 133px;
    font-family: 'Oswald', 'Arial Narrow', sans-serif;
    font-size: 17px; line-height: 20px;
    color: var(--white);
    white-space: nowrap;
  }
  .nutrition-note {
    position: absolute; left: 424px; top: 125px;
    width: 84px;
    font-family: 'Open Sans', Arial, sans-serif;
    font-size: 8px; line-height: 10px;
    color: var(--white);
    text-align: center;
    text-transform: uppercase;
    letter-spacing: 0.2px;
  }
  .title-rabbits {
    position: absolute; left: 12px; top: 163px;
    font-family: 'Noticia Text', Georgia, serif;
    font-style: italic;
    font-size: 92px; line-height: 1;
    color: var(--white);
    letter-spacing: 2px;
    white-space: nowrap;
  }
  .seal-spaces { position: absolute; left: 413px; top: 17px; }
  .rabbit-art {
    position: absolute;
    left: 372px; top: 176px;
    width: 124px; height: 92px;
    border-radius: 10px;
    background: linear-gradient(to bottom, var(--white) 0%, var(--art-shade) 100%);
  }
</style>
</head>
<body>
  <div class="label">
    <div class="band band--pasture" role="img" aria-label="Pink-tinted photo of a farm pasture with trees and a farmhouse"></div>
    <div class="band band--cut"></div>
    <div class="band band--name"></div>

    <div class="title-farm">farm raised</div>

    <svg class="seal-spaces" width="86" height="86" viewBox="0 0 86 86" aria-label="Spaces for inspection seals">
      <circle cx="19" cy="19" r="17" fill="var(--seal-gold)" stroke="var(--white)" stroke-width="1.5"/>
      <circle cx="66" cy="19" r="17" fill="var(--seal-gold)" stroke="var(--white)" stroke-width="1.5"/>
      <circle cx="19" cy="66" r="17" fill="var(--seal-gold)" stroke="var(--white)" stroke-width="1.5"/>
      <circle cx="66" cy="66" r="17" fill="var(--seal-gold)" stroke="var(--white)" stroke-width="1.5"/>
    </svg>

    <p class="cut-description">Whole cut-up with 2 fore-legs, 2 hind legs and back.</p>

    <p class="nutrition-note">Nutritional<br>information<br>on the back</p>

    <div class="title-rabbits">Rabbits</div>

    <div class="rabbit-art" role="img" aria-label="White silhouette of a sitting rabbit"></div>
  </div>
</body>
</html>
```